Velvet Orchard

We need a business card design for a new project that we are openning.

Industry/Entity Type

Business

Contact Information for Business Card

Business Card

```html
<!DOCTYPE html>
<html lang="en">
<head>
<meta charset="utf-8">
<title>Velvet Orchard – Business Cards</title>
<link rel="stylesheet" href="https://fonts.googleapis.com/css2?family=Kaushan+Script&family=Alegreya:ital,wght@1,500;1,700&family=Alegreya+Sans:wght@400&family=Roboto:wght@300&display=swap">
<style>
  :root{
    --bg-light:#e6f8e2;
    --bg-edge:#b9e6b3;
    --green-center:#22a044;
    --green-mid:#11502a;
    --green-edge:#0d2416;
    --red-center:#cc0620;
    --red-mid:#82061a;
    --red-edge:#2e0a10;
    --title-green:#c4eeb0;
    --white:#ffffff;
    --yellow:#f5e83a;
    --contact-grey:#e2e2e2;
    --tag-green-top:#2fb52f;
    --tag-green-bottom:#0f7a14;
    --tag-blue-top:#2f56c8;
    --tag-blue-bottom:#14297e;
    --ring-green:#2fbf3a;
    --ring-blue:#3a9ae8;
  }
  *{margin:0;padding:0;box-sizing:border-box;}
  html,body{width:991px;height:1200px;overflow:hidden;}
  body{
    background:radial-gradient(ellipse at 50% 50%, var(--bg-light) 0%, #d2f1cc 70%, var(--bg-edge) 100%);
    position:relative;
    font-family:"Alegreya Sans", sans-serif;
  }
  .card{
    position:absolute;left:88px;width:815px;height:467px;
    box-shadow:0 6px 18px rgba(0,0,0,.35);
    overflow:hidden;
  }
  .card--pt{top:113px;background:radial-gradient(ellipse 560px 420px at 691px 212px, var(--green-center) 0%, var(--green-mid) 55%, var(--green-edge) 100%);}
  .card--en{top:619px;background:radial-gradient(ellipse 620px 440px at 549px 231px, var(--red-center) 0%, var(--red-mid) 55%, var(--red-edge) 100%);}

  .flag{position:absolute;left:33px;top:33px;width:205px;height:127px;}
  .card--pt .flag{background:linear-gradient(135deg,#1d7a2e,#e9d31a 50%,#1d7a2e);}
  .card--en .flag{left:-6px;top:32px;width:214px;height:129px;background:linear-gradient(135deg,#1b2a7a,#22307e);}

  .brand{
    position:absolute;left:259px;top:50px;
    font-family:"Kaushan Script", cursive;font-size:62px;line-height:1;white-space:nowrap;
  }
  .card--pt .brand{color:var(--title-green);}
  .card--en .brand{color:var(--white);top:58px;}

  .tagline{
    position:absolute;left:44px;
    font-family:"Alegreya", serif;font-style:italic;font-weight:500;
    font-size:32px;line-height:40px;color:var(--yellow);
  }
  .card--pt .tagline{top:178px;}
  .card--en .tagline{left:44px;top:206px;}

  .contacts{
    position:absolute;left:552px;top:187px;
    font-family:"Roboto", sans-serif;font-weight:300;font-size:20px;line-height:28.5px;
    color:var(--contact-grey);list-style:none;
  }
  .card--en .contacts{top:188px;}
  .contacts li{display:flex;}
  .contacts .name{width:68px;}
  .contacts li:last-child .name{width:60px;}

  .address{
    position:absolute;left:28px;top:330px;
    font-size:21px;line-height:28px;color:var(--white);font-style:normal;
  }

  .products{position:absolute;left:0;top:0;list-style:none;}
  .product{position:absolute;top:272px;width:143px;height:172px;}
  .product:nth-child(1){left:183px;}
  .product:nth-child(2){left:337px;}
  .product:nth-child(3){left:490px;}
  .product:nth-child(4){left:644px;}
  .product .photo{
    position:absolute;left:0;top:0;width:143px;height:143px;border-radius:50%;
    border:3px solid var(--ring-green);
  }
  .card--en .product .photo{border-color:var(--ring-blue);}
  .photo--meat{background:radial-gradient(circle,#b8323a,#6e1a20);}
  .photo--skewer{background:radial-gradient(circle,#c46a38,#7a3a1e 70%,#e8e0d8);}
  .photo--coil{background:radial-gradient(circle,#c2502e,#8a2e1a);}
  .photo--spice{background:radial-gradient(circle,#f2f2f2,#c9a07a 60%,#e8e8e8);}
  .product .label{
    position:absolute;left:0;top:137px;width:143px;height:33px;border-radius:5px;
    display:flex;align-items:center;justify-content:center;
    font-family:"Alegreya", serif;font-style:italic;font-weight:700;font-size:20px;
    color:var(--yellow);
  }
  .card--pt .label{background:linear-gradient(var(--tag-green-top),var(--tag-green-bottom));}
  .card--en .label{background:linear-gradient(var(--tag-blue-top),var(--tag-blue-bottom));}
</style>
</head>
<body>

<section class="card card--pt" lang="pt">
  <div class="flag" role="img" aria-label="Brazilian national flag"></div>
  <h1 class="brand">Velvet Orchard</h1>
  <p class="tagline">Liguem e faca a sua<br>encomenda!</p>
  <ul class="contacts">
    <li><span class="name">Marlow:</span><span>&nbsp;&nbsp;&nbsp;0412557803</span></li>
    <li><span class="name">Tobias:</span><span>&nbsp;&nbsp;&nbsp;0419246631</span></li>
    <li><span class="name">Renata:</span><span>&nbsp;&nbsp;(07) 5550 1284</span></li>
  </ul>
  <address class="address">14/58<br>Linden Road<br>Marrowvale, QLD<br>4299, Brisbane</address>
  <ul class="products">
    <li class="product"><div class="photo photo--meat" role="img" aria-label="Photo of dried salted beef"></div><span class="label">Charque</span></li>
    <li class="product"><div class="photo photo--skewer" role="img" aria-label="Photo of grilled sausages on skewers"></div><span class="label">Linguica</span></li>
    <li class="product"><div class="photo photo--coil" role="img" aria-label="Photo of a coiled sausage"></div><span class="label">Espetinhos</span></li>
    <li class="product"><div class="photo photo--spice" role="img" aria-label="Photo of spice jars"></div><span class="label">Semperos</span></li>
  </ul>
</section>

<section class="card card--en" lang="en">
  <div class="flag" role="img" aria-label="Australian national flag"></div>
  <h2 class="brand">Velvet Orchard</h2>
  <p class="tagline">Call and make your order</p>
  <ul class="contacts">
    <li><span class="name">Marlow:</span><span>&nbsp;&nbsp;&nbsp;0412557803</span></li>
    <li><span class="name">Tobias:</span><span>&nbsp;&nbsp;&nbsp;0419246631</span></li>
    <li><span class="name">Renata:</span><span>&nbsp;&nbsp;(07) 5550 1284</span></li>
  </ul>
  <address class="address">14/58<br>Linden Road<br>Marrowvale, QLD<br>4299, Brisbane</address>
  <ul class="products">
    <li class="product"><div class="photo photo--meat" role="img" aria-label="Photo of dried salted beef"></div><span class="label">Chack</span></li>
    <li class="product"><div class="photo photo--skewer" role="img" aria-label="Photo of grilled sausages on skewers"></div><span class="label">Sausage</span></li>
    <li class="product"><div class="photo photo--coil" role="img" aria-label="Photo of a coiled sausage"></div><span class="label">Skewers</span></li>
    <li class="product"><div class="photo photo--spice" role="img" aria-label="Photo of spice jars"></div><span class="label">Spices</span></li>
  </ul>
</section>

</body>
</html>
```